Book cover for a book on tactics, habits and directives learned from world class performers

The Quiet Ledger book is the first in a series of four books filled with proven tactics, habits and directives (i.e., what to do) that young, ambitious working professionals should be doing to make their life better. The first book is on foundational or keystone habits - that is, the habits that will help everyone upgrade their life and enable other great habits in their life (things such as waking up early in the morning or exercising)

The goal of the book is to stand out on the Brimvale platform as a small thumbnail, as well as a 5 x 8 book.

The imagery should make the viewer feel that the book (and the author) are the authority in habits and developing habits.

The reader should feel that they must have this book if they know they should be developing successful habits but do not want to comb through hundreds of books just to find the one tactic or habit that they should be doing. It's important that the book "pops off the shelf" and catches the eye quickly.

The most important part of the design is that it sells, not that it looks well-designed. I am open to any image or illustration you choose though please consider the nice have I have listed below. Here are a few words that come to mind when thinking of my book: growth, self development, leadership, success, freedom, passion, motivation, young professional, accomplished, experience.

I like a bold color palette. I like bold titles that you know right away what the title is and what it is about, not too busy and with simple color schemes. 2 - 3 colors.

Books with covers I like:
- Lamp Orchard by Norris Pellaquin
- Under The Copper Tide by Gordon Pruitt
- The Velvet Compass by Edgar Fulbright

Target Market(s)

- Young 20 - 40 year old ambitious working professionals interested in self development and listen to podcasts of Ned Caplow, Rufus Denholme
- Just starting out management consultants

Colors

Designer to choose colors to be used in the design.

Requirements
Must have
• 'Quiet Ledger' title - first and foremost
• Author name - Lu Qiao - probably on the bottom or somewhere
• Bold colour / colours or a graphic that is eye catching (and makes it different from other habits books on Brimvale)
Nice to have
• Would like to have some sort of visual, colour or theme that can run through the four books - would be great to have a cover design that can be simply changed to depict the second, third or fourth book in the series - maybe the graphic or visual can be changed with some colours, etc. but with the overall feel looking similar so that people can see that it's part of the same book series

```html
<!DOCTYPE html>
<html lang="en">
<head>
<meta charset="utf-8">
<title>Quiet Ledger — Lu Qiao</title>
<link rel="stylesheet" href="https://fonts.googleapis.com/css2?family=Cinzel:wght@400&family=Bebas+Neue&display=swap">
<style>
  :root {
    --glow: #fdf7e6;
    --haze: #f1dfc4;
    --dusk: #9a7470;
    --mauve: #7f5e5c;
    --petal: #e9d6bd;
    --meadow: #b8a98a;
    --title-brown: #734631;
    --author-ink: #241a14;
  }
  html, body {
    margin: 0;
    padding: 0;
    overflow: hidden;
    background: #ffffff;
  }
  .cover {
    position: relative;
    width: 737px;
    height: 1200px;
    overflow: hidden;
  }
  .cover-photo {
    position: absolute;
    inset: 0;
    background:
      radial-gradient(ellipse 70% 22% at 50% 12%, var(--glow) 0%, rgba(253,247,230,0.9) 45%, rgba(253,247,230,0) 100%),
      radial-gradient(circle 90px at 48% 47%, rgba(250,244,232,0.85) 0%, rgba(250,244,232,0) 100%),
      radial-gradient(ellipse 40% 14% at 20% 72%, rgba(240,226,205,0.7) 0%, rgba(240,226,205,0) 100%),
      radial-gradient(ellipse 30% 12% at 88% 76%, rgba(240,228,210,0.7) 0%, rgba(240,228,210,0) 100%),
      linear-gradient(180deg,
        var(--glow) 0%,
        var(--haze) 22%,
        #c9a89a 32%,
        var(--dusk) 40%,
        var(--mauve) 48%,
        #a58a7c 58%,
        var(--petal) 70%,
        #d7c6a8 82%,
        var(--meadow) 100%);
  }
  .author {
    position: absolute;
    top: 62px;
    left: 0;
    right: 0;
    margin: 0;
    text-align: center;
    font-family: 'Cinzel', serif;
    font-weight: 400;
    font-size: 60px;
    letter-spacing: 0.32em;
    padding-left: 0.32em;
    color: var(--author-ink);
    line-height: 1;
  }
  .title {
    position: absolute;
    left: 0;
    right: 0;
    top: 752px;
    margin: 0;
    text-align: center;
    font-family: 'Bebas Neue', sans-serif;
    font-weight: 400;
    color: var(--title-brown);
    line-height: 1;
  }
  .title-kicker {
    display: block;
    font-size: 104px;
    letter-spacing: 0.42em;
    padding-left: 0.42em;
    line-height: 0.9;
  }
  .title-main {
    display: block;
    font-size: 292px;
    letter-spacing: 0.02em;
    line-height: 0.86;
  }
</style>
</head>
<body>
  <main class="cover">
    <div class="cover-photo" role="img" aria-label="Soft-focus photograph of a white daisy in a sunlit meadow, warm backlit glow behind"></div>
    <p class="author">LU QIAO</p>
    <h1 class="title">
      <span class="title-kicker">QUIET</span>
      <span class="title-main">LEDGER</span>
    </h1>
  </main>
</body>
</html>
```